We need a logo and landing page designed. We are a full-service general contractor based in Tempe Arizona. We can provide all phases of construction from design to completion. We specialize in commercial and residential remodels, as well as ground-up construction. We will like to see designs that primarily used reds, blues, blacks, whites, etc. The design should be a professional yet fun, easy-to-read format. Our name is Oak Harbor Construction...I would like to see some designs that incorporate a "oak harbor" and some without.
The final design should communicate a professional, quality-driven, safety oriented full service business.

Target Market(s)

Building owners, land developers, homeowners

Industry/Entity Type

Commercial Construction

Coding

Coded - Design and coding required

Number of Pages Required

1 page

Font styles to use
Serif

Colors
0054AA
0677BA
7BADD7
CADEEF
E8F1F8
59FF00
82FF00
B8FF75
E3FFCB
F4FFEA
EE7325
F08F49
F5BC92
FAE3D3
FDF4ED
EB3D1F
EC4F4E
F09395
F8D3D4
FCEDEE

```html
<!DOCTYPE html>
<html lang="en">
<head>
<meta charset="utf-8">
<title>Oak Harbor Construction</title>
<link rel="stylesheet" href="https://fonts.googleapis.com/css2?family=Playfair+Display:wght@400;700&family=Lato:wght@400;700&display=swap">
<style>
:root{
  --orange:#EE7325;
  --orange-soft:#F08F49;
  --ink:#1e1e1e;
  --dark:#232323;
  --text:#4a4a4a;
  --muted:#6b6b6b;
  --light:#f1f1f1;
  --white:#ffffff;
  --star:#f5c400;
  --card-blue:#2f3d52;
}
*{box-sizing:border-box;margin:0;padding:0}
html,body{width:1200px;height:4901px;overflow:hidden}
body{font-family:"Lato",Arial,sans-serif;color:var(--text);background:var(--white);position:relative}
.serif{font-family:"Playfair Display",Georgia,serif}
.abs{position:absolute}
section,header,footer{position:absolute;left:0;width:1200px;overflow:hidden}
.label{font-size:14px;letter-spacing:.5px;text-transform:uppercase;color:var(--ink)}
.h2{font-family:"Playfair Display",Georgia,serif;font-weight:700;font-size:34px;color:var(--ink)}
.center{text-align:center;left:0;width:1200px}
.link-line{font-family:"Playfair Display",Georgia,serif;color:var(--orange);font-size:16px;font-weight:700;display:flex;align-items:center;gap:12px}
.link-line::before{content:"";width:24px;height:2px;background:var(--orange)}
.btn-outline{border:2px solid var(--orange);color:var(--orange);font-family:"Playfair Display",Georgia,serif;font-weight:700;font-size:16px;display:flex;align-items:center;justify-content:center}
.logo{font-family:"Playfair Display",Georgia,serif;font-weight:700;font-size:38px;color:var(--white);letter-spacing:-.5px}

/* hero */
.hero{top:0;height:600px;background:linear-gradient(115deg,#3a4452 0%,#4c5a66 40%,#5d6a68 60%,#2d3338 100%)}
.hero-photo{position:absolute;inset:0;background:linear-gradient(90deg,rgba(20,24,30,.75) 0%,rgba(30,35,40,.35) 55%,rgba(40,45,50,.15) 100%)}
.topbar{top:0;height:23px;background:rgba(0,0,0,.35);font-size:10px;color:#ddd}
.topbar .item{position:absolute;top:5px;display:flex;gap:6px;align-items:center}
.social{position:absolute;top:5px;right:130px;display:flex;gap:10px}
.social span{width:10px;height:10px;border-radius:50%;background:var(--orange)}
.nav{position:absolute;top:52px;left:541px;display:flex;gap:0;font-family:"Playfair Display",Georgia,serif;font-size:15px;color:var(--white)}
.nav a{color:var(--white);text-decoration:none;margin-right:36px}
.nav .cta{background:var(--orange);padding:9px 22px;margin-left:6px;margin-right:0;margin-top:-8px}
.hero h1{position:absolute;left:129px;top:172px;font-family:"Playfair Display",Georgia,serif;font-weight:700;font-size:64px;line-height:70px;color:var(--white)}
.hero p{position:absolute;left:129px;top:322px;width:340px;font-size:15px;line-height:22px;color:#eee}

/* about */
.about{top:600px;height:547px;background:var(--light)}
.photo{position:absolute;box-shadow:0 10px 30px rgba(0,0,0,.25)}
.about .text{position:absolute;left:675px;top:146px;width:390px}
.about h2{font-size:32px;margin:8px 0 26px}
.about p{font-size:13px;line-height:21px;color:var(--text);margin-bottom:26px}

/* what we do */
.what{top:1147px;height:508px;background:var(--white)}
.steps{position:absolute;top:344px;left:129px;width:942px;display:flex;justify-content:space-between}
.step{display:flex;gap:18px;width:280px}
.step .ic{width:46px;height:46px;border-radius:50%;background:var(--orange);flex:none;display:flex;align-items:center;justify-content:center}
.step h4{font-size:13px;font-weight:700;color:var(--ink);margin-bottom:6px;margin-top:6px}
.step p{font-size:12px;line-height:16px;color:var(--muted)}
.dots{position:absolute;top:360px;color:var(--orange);font-size:12px;letter-spacing:2px}

/* services */
.services{top:1655px;height:609px;background:linear-gradient(180deg,#2b2e33,#3a3d42 50%,#222 100%)}
.services .label,.services .h2{color:var(--white)}
.card{position:absolute;top:234px;width:215px;height:180px;background:rgba(47,61,82,.8);border:1px solid rgba(120,150,190,.45);display:flex;flex-direction:column;align-items:center;justify-content:center;gap:14px;color:var(--white);font-family:"Playfair Display",Georgia,serif;font-weight:700;font-size:19px;line-height:26px;text-align:center}
.card .ic{width:48px;height:48px;border-radius:50%;background:var(--orange)}

/* testimonials */
.testi{top:2264px;height:490px;background:var(--white)}
.quote{position:absolute;top:224px;width:425px}
.stars{color:var(--star);font-size:15px;letter-spacing:1px}
.quote p{font-size:13px;line-height:22px;color:var(--text);margin:12px 0 18px}
.author{display:flex;gap:14px;align-items:center}
.avatar{width:32px;height:32px;border-radius:50%;background:linear-gradient(135deg,#e9d9cc,#b89a86)}
.author b{display:block;font-family:"Playfair Display",Georgia,serif;color:var(--ink);font-size:14px}
.author span{font-size:12px}
.arrows{position:absolute;top:150px;left:994px;display:flex;gap:8px}
.arrows span{width:28px;height:28px;border-radius:50%;border:1px solid #ddd;color:var(--orange-soft);font-size:12px;display:flex;align-items:center;justify-content:center}

/* projects + areas */
.projects{top:2754px;height:1208px;background:linear-gradient(180deg,#efefef,#f4f4f4)}
.pcard{position:absolute;width:232px;overflow:hidden}
.pcard .cap{position:absolute;left:0;bottom:0;width:100%;padding:0 22px 18px;color:var(--white);background:linear-gradient(180deg,transparent,rgba(0,0,0,.7))}
.pcard h4{font-family:"Playfair Display",Georgia,serif;font-size:16px;margin-bottom:6px}
.pcard p{font-size:12px;line-height:16px}
.divider{position:absolute;top:632px;left:129px;width:942px;height:1px;background:#d8d8d8}
.map{position:absolute;left:129px;top:803px;width:598px;height:323px;background:linear-gradient(135deg,#ececec,#dcdcdc);border:4px solid var(--white);box-shadow:0 4px 14px rgba(0,0,0,.15)}
.areas{position:absolute;left:727px;top:841px;width:342px;height:247px;background:var(--orange-soft);padding:26px 28px;color:var(--white)}
.areas p{font-size:13px;line-height:19px;margin-bottom:12px}
.areas ul{list-style:none;display:grid;grid-template-columns:1fr 1fr;row-gap:10px}
.areas li{font-size:14px;font-weight:700;display:flex;gap:8px;align-items:center}

/* contact */
.contact{top:3962px;height:574px;background:linear-gradient(180deg,#2e3135,#3c4044 55%,#2a2c2f)}
.contact .label,.contact .h2{color:var(--white)}
.contact .intro{top:171px;font-size:13px;line-height:21px;color:#ddd}
.field{position:absolute;border-bottom:1px solid #bbb;color:var(--white);font-size:12px;padding-bottom:18px}
.field i{color:var(--orange);font-style:normal}
.submit{position:absolute;left:544px;top:432px;width:110px;height:32px;background:var(--orange);color:var(--white);font-family:"Playfair Display",Georgia,serif;font-size:14px;display:flex;align-items:center;justify-content:center}

/* footer */
footer{top:4536px;height:365px;background:var(--dark);color:#cfcfcf}
footer h5{font-family:"Playfair Display",Georgia,serif;font-size:15px;color:var(--white);margin-bottom:16px}
.col{position:absolute;top:64px}
.col ul{list-style:none}
.col li{font-size:14px;line-height:30px;color:#ddd}
.contact-info li{font-size:12px;line-height:16px;margin-bottom:10px}
.contact-info b{display:flex;gap:8px;align-items:center;color:var(--white);font-size:13px;margin-bottom:3px}
.copy{position:absolute;left:129px;top:328px;width:942px;font-size:11px;display:flex;justify-content:space-between;border-top:1px solid #3a3a3a;padding-top:16px}
.copy em{color:var(--orange);font-style:normal}
</style>
</head>
<body>

<header class="hero">
  <div class="hero-photo" role="img" aria-label="Modern glass and concrete apartment building against a cloudy sky"></div>
  <div class="abs topbar" style="left:0;width:1200px;position:absolute">
    <div class="item" style="left:131px"><svg width="9" height="10" viewBox="0 0 10 12"><path d="M5 0a4 4 0 0 0-4 4c0 3 4 8 4 8s4-5 4-8a4 4 0 0 0-4-4z" fill="#EE7325"/></svg>1480 Mesa Vista Ave. Tempe, Arizona 85281</div>
    <div class="item" style="left:400px"><svg width="10" height="10" viewBox="0 0 12 12"><path d="M2 1l2 0 1 3-1.5 1a7 7 0 0 0 3.5 3.5L8 7l3 1v2a1 1 0 0 1-1 1A9 9 0 0 1 1 2a1 1 0 0 1 1-1z" fill="#EE7325"/></svg>(480) 555-0192</div>
    <div class="social"><span></span><span></span><span></span><span></span></div>
  </div>
  <div class="logo abs" style="left:129px;top:38px">OakHarbor</div>
  <nav class="nav"><a>Home</a><a>About Us</a><a>Services</a><a>Projects</a><a class="cta">Contact Us</a></nav>
  <h1>We Are Build<br>Your World</h1>
  <p>We specialize in commercial and residential remodels, as well as ground-up construction</p>
  <div class="btn-outline abs" style="left:129px;top:396px;width:246px;height:56px">Request An Appointment</div>
  <svg class="abs" style="left:0;top:500px" width="1200" height="100" viewBox="0 0 1200 100" preserveAspectRatio="none">
    <polygon points="0,100 0,82 1200,4 1200,26" fill="#EE7325"/>
    <polygon points="0,100 1200,26 1200,100" fill="#f1f1f1"/>
  </svg>
</header>

<section class="about">
  <div class="photo" style="left:129px;top:128px;width:234px;height:332px;background:linear-gradient(160deg,#cfe3f3,#9fb9cf 50%,#7a5040)" role="img" aria-label="Tower crane beside a brick building under construction"></div>
  <div class="photo" style="left:377px;top:89px;width:232px;height:332px;background:linear-gradient(200deg,#6b8fb5,#3e5f86 50%,#223a5a)" role="img" aria-label="Glass skyscraper viewed from below"></div>
  <div class="text">
    <div class="label">About Us</div>
    <h2 class="h2 about-title">Oak Harbor Construction</h2>
    <p>Lorem ipsum dolor sit amet, consectetur adipiscing elit. Pharetra faucibus fames sed ac volutpat ligula faucibus elit natoque. Ornare ultrices sed nisl vestibulum. In montes, eget mauris non duis nunc. Ultrices lacinia enim..</p>
    <div class="link-line">Learn More</div>
  </div>
</section>

<section class="what">
  <div class="abs center label" style="top:114px">What We Do</div>
  <div class="abs center h2" style="top:140px">More Than Just A Contractor</div>
  <p class="abs" style="left:260px;width:680px;top:196px;text-align:center;font-size:13px;line-height:21px">Lorem ipsum dolor sit amet, consectetur adipiscing elit. Pharetra faucibus fames sed ac volutpat ligula faucibus elit natoque. Ornare ultrices sed nisl vestibulum. In montes, eget mauris non duis nunc. Ultrices lacinia enim, a, cursus lobortis viverra. Et, nibh tortor pellentesque vestibulum dui.</p>
  <div class="abs center serif" style="top:296px;font-size:19px;font-weight:700;color:var(--ink)">Here Is How We Do It</div>
  <div class="steps">
    <div class="step"><div class="ic"><svg width="20" height="20" viewBox="0 0 20 20"><rect x="4" y="3" width="12" height="14" fill="none" stroke="#fff" stroke-width="2"/><path d="M7 8h6M7 12h6" stroke="#fff" stroke-width="2"/></svg></div><div><h4>Ornare ultrices sed</h4><p>Lorem ipsum dolor sit amet, consectetur adipiscing elit pharetra faucibus fames</p></div></div>
    <div class="step"><div class="ic"><svg width="20" height="20" viewBox="0 0 20 20"><path d="M3 17V7l7-4 7 4v10z" fill="none" stroke="#fff" stroke-width="2"/></svg></div><div><h4>Ornare ultrices sed</h4><p>Lorem ipsum dolor sit amet, consectetur adipiscing elit pharetra faucibus fames</p></div></div>
    <div class="step"><div class="ic"><svg width="20" height="20" viewBox="0 0 20 20"><path d="M2 10l8-7 8 7M5 8v9h10V8" fill="none" stroke="#fff" stroke-width="2"/></svg></div><div><h4>Ornare ultrices sed</h4><p>Lorem ipsum dolor sit amet, consectetur adipiscing elit pharetra faucibus fames</p></div></div>
  </div>
  <div class="dots" style="left:396px">· · &gt; · ·</div>
  <div class="dots" style="left:736px">· · &gt; · ·</div>
</section>

<section class="services">
  <div class="abs" style="inset:0;background:linear-gradient(90deg,rgba(0,0,0,.25),rgba(0,0,0,0) 50%,rgba(0,0,0,.3))" role="img" aria-label="Dark-toned street view of modern apartment blocks"></div>
  <svg class="abs" style="left:0;top:0" width="1200" height="100" viewBox="0 0 1200 100" preserveAspectRatio="none">
    <polygon points="0,0 1200,0 1200,0 0,80" fill="#ffffff"/>
    <polygon points="0,80 1200,0 1200,24 0,104" fill="#EE7325"/>
  </svg>
  <div class="abs center label" style="top:142px">Services</div>
  <div class="abs center h2" style="top:168px">Oak Harbor Services</div>
  <div class="card" style="left:129px"><span class="ic"></span>Residential<br>Remodels</div>
  <div class="card" style="left:371px"><span class="ic"></span>Commercial<br>Remodels</div>
  <div class="card" style="left:612px"><span class="ic"></span>Ground-Up<br>Construction</div>
  <div class="card" style="left:852px"><span class="ic"></span>Remodels<br>Consulting</div>
  <div class="btn-outline abs" style="left:477px;top:472px;width:244px;height:55px">Request An Appointment</div>
</section>

<section class="testi">
  <div class="abs label" style="left:129px;top:118px">Testimonials</div>
  <div class="abs h2" style="left:129px;top:144px">What Our Customer Say</div>
  <div class="abs" style="left:633px;top:164px;width:350px;height:1px;background:#ddd"></div>
  <div class="arrows"><span>&lt;</span><span>&gt;</span></div>
  <div class="quote" style="left:129px">
    <div class="stars">★★★★★</div>
    <p>Lorem ipsum dolor sit amet, consectetur adipiscing elit. Scelerisque a malesuada egestas non facilisis risus id nisi, tellus. Sed pellentesque iaculis in varius velit. Eget pellentesque libero, turpis tellus nibh ut tellus.</p>
    <div class="author"><div class="avatar" role="img" aria-label="Customer portrait"></div><div><b>Clara Whitfield</b><span>Lorem ipsum</span></div></div>
  </div>
  <div class="quote" style="left:633px">
    <div class="stars">★★★★★</div>
    <p>Lorem ipsum dolor sit amet, consectetur adipiscing elit. Scelerisque a malesuada egestas non facilisis risus id nisi, tellus. Sed pellentesque iaculis in varius velit. Eget pellentesque libero, turpis tellus nibh ut tellus.</p>
    <div class="author"><div class="avatar" role="img" aria-label="Customer portrait"></div><div><b>Clara Whitfield</b><span>Lorem ipsum</span></div></div>
  </div>
</section>

<section class="projects">
  <div class="abs center label" style="top:74px">Projects</div>
  <div class="abs center h2" style="top:100px">Our Resent Projects</div>
  <div class="pcard" style="left:129px;top:192px;height:298px;background:linear-gradient(180deg,#9aa8b6,#5a4b44 55%,#3a3532)" role="img" aria-label="Modern brick and dark-clad townhouse">
    <div class="cap"><h4>Lorem Ipsum Dolor</h4><p>Lorem ipsum dolor sit amet, consectetur adipiscing elit.</p></div></div>
  <div class="pcard" style="left:366px;top:174px;height:298px;background:linear-gradient(180deg,#b9cde0,#8c8f8c 45%,#5d4a3a)" role="img" aria-label="Two-storey family house with porch">
    <div class="cap"><h4>Lorem Ipsum Dolor</h4><p>Lorem ipsum dolor sit amet, consectetur adipiscing elit.</p></div></div>
  <div class="pcard" style="left:601px;top:214px;height:298px;background:linear-gradient(180deg,#8fb7d8,#8a7a70 45%,#3c3532)" role="img" aria-label="Apartment tower with balconies">
    <div class="cap"><h4>Lorem Ipsum Dolor</h4><p>Lorem ipsum dolor sit amet, consectetur adipiscing elit.</p></div></div>
  <div class="pcard" style="left:837px;top:192px;height:298px;background:linear-gradient(180deg,#a9c8e6,#4f6d92 50%,#2c3e55)" role="img" aria-label="Glass office buildings">
    <div class="cap"><h4>Lorem Ipsum Dolor</h4><p>Lorem ipsum dolor sit amet, consectetur adipiscing elit.</p></div></div>
  <div class="abs center" style="top:550px;display:flex;justify-content:center"><div class="link-line">View All Projects</div></div>
  <div class="divider"></div>
  <div class="abs center label" style="top:719px">Projects</div>
  <div class="abs center h2" style="top:745px">Areas We Served</div>
  <div class="map" role="img" aria-label="Street map of the service area"></div>
  <div class="areas">
    <p>Lorem ipsum dolor sit amet, consectetur adipiscing elit. Scelerisque a malesuada egestas non facilisis risus id nisi, tellus.</p>
    <ul>
      <li><svg width="10" height="12" viewBox="0 0 10 12"><path d="M5 0a4 4 0 0 0-4 4c0 3 4 8 4 8s4-5 4-8a4 4 0 0 0-4-4z" fill="#fff"/></svg>Lorem ipsum</li>
      <li><svg width="10" height="12" viewBox="0 0 10 12"><path d="M5 0a4 4 0 0 0-4 4c0 3 4 8 4 8s4-5 4-8a4 4 0 0 0-4-4z" fill="#fff"/></svg>Lorem ipsum</li>
      <li><svg width="10" height="12" viewBox="0 0 10 12"><path d="M5 0a4 4 0 0 0-4 4c0 3 4 8 4 8s4-5 4-8a4 4 0 0 0-4-4z" fill="#fff"/></svg>Lorem ipsum</li>
      <li><svg width="10" height="12" viewBox="0 0 10 12"><path d="M5 0a4 4 0 0 0-4 4c0 3 4 8 4 8s4-5 4-8a4 4 0 0 0-4-4z" fill="#fff"/></svg>Lorem ipsum</li>
      <li><svg width="10" height="12" viewBox="0 0 10 12"><path d="M5 0a4 4 0 0 0-4 4c0 3 4 8 4 8s4-5 4-8a4 4 0 0 0-4-4z" fill="#fff"/></svg>Lorem ipsum</li>
      <li><svg width="10" height="12" viewBox="0 0 10 12"><path d="M5 0a4 4 0 0 0-4 4c0 3 4 8 4 8s4-5 4-8a4 4 0 0 0-4-4z" fill="#fff"/></svg>Lorem ipsum</li>
      <li><svg width="10" height="12" viewBox="0 0 10 12"><path d="M5 0a4 4 0 0 0-4 4c0 3 4 8 4 8s4-5 4-8a4 4 0 0 0-4-4z" fill="#fff"/></svg>Lorem ipsum</li>
      <li><svg width="10" height="12" viewBox="0 0 10 12"><path d="M5 0a4 4 0 0 0-4 4c0 3 4 8 4 8s4-5 4-8a4 4 0 0 0-4-4z" fill="#fff"/></svg>Lorem ipsum</li>
      <li><svg width="10" height="12" viewBox="0 0 10 12"><path d="M5 0a4 4 0 0 0-4 4c0 3 4 8 4 8s4-5 4-8a4 4 0 0 0-4-4z" fill="#fff"/></svg>Lorem ipsum</li>
      <li><svg width="10" height="12" viewBox="0 0 10 12"><path d="M5 0a4 4 0 0 0-4 4c0 3 4 8 4 8s4-5 4-8a4 4 0 0 0-4-4z" fill="#fff"/></svg>Lorem ipsum</li>
    </ul>
  </div>
</section>

<section class="contact">
  <div class="abs" style="inset:0;background:linear-gradient(90deg,rgba(0,0,0,.2),rgba(0,0,0,.05) 50%,rgba(0,0,0,.25))" role="img" aria-label="Dimmed photo of modern residential buildings"></div>
  <div class="abs center label" style="top:89px">Contact Us</div>
  <div class="abs center h2" style="top:115px">Let Us Assist You</div>
  <p class="abs center intro" style="padding:0 380px;text-align:center">Lorem ipsum dolor sit amet, consectetur adipiscing elit. Scelerisque a malesuada egestas non facilisis risus id nisi, tellus.</p>
  <div class="field" style="left:290px;top:232px;width:296px">Name <i>*</i></div>
  <div class="field" style="left:610px;top:232px;width:302px">Phone <i>*</i></div>
  <div class="field" style="left:290px;top:285px;width:622px">Email <i>*</i></div>
  <div class="field" style="left:290px;top:352px;width:622px;padding-bottom:38px">Your message</div>
  <div class="submit">Submit</div>
  <svg class="abs" style="left:0;top:494px" width="1200" height="80" viewBox="0 0 1200 80" preserveAspectRatio="none">
    <polygon points="0,80 1200,0 1200,22 0,80" fill="#EE7325"/>
    <polygon points="0,80 1200,22 1200,80" fill="#232323"/>
  </svg>
</section>

<footer>
  <div class="logo abs" style="left:129px;top:66px">OakHarbor</div>
  <p class="abs" style="left:129px;top:132px;width:220px;font-size:11px;line-height:15px">Lorem ipsum dolor sit amet, consectetur adipiscing elit pharetra faucibus fames</p>
  <div class="abs" style="left:131px;top:190px;display:flex;gap:18px">
    <span style="width:14px;height:14px;border-radius:50%;background:var(--orange)"></span>
    <span style="width:14px;height:14px;border-radius:50%;background:var(--orange)"></span>
    <span style="width:14px;height:14px;border-radius:50%;background:var(--orange)"></span>
    <span style="width:14px;height:14px;border-radius:50%;background:var(--orange)"></span>
  </div>
  <div class="col" style="left:413px"><h5>Quick Links</h5><ul><li>Home</li><li>About Us</li><li>Services</li><li>Projects</li><li>Contact Us</li></ul></div>
  <div class="col" style="left:611px"><h5>Customer Services</h5><ul><li>Residential Remodels</li><li>Commercial Remodels</li><li>Ground-Up Construction</li><li>Remodels Consulting</li></ul></div>
  <div class="col contact-info" style="left:886px;width:190px"><h5>Our Contact Info</h5><ul>
    <li><b><svg width="11" height="13" viewBox="0 0 10 12"><path d="M5 0a4 4 0 0 0-4 4c0 3 4 8 4 8s4-5 4-8a4 4 0 0 0-4-4z" fill="#EE7325"/></svg>Location</b>1480 Mesa Vista Ave. Tempe, Arizona 85281</li>
    <li><b><svg width="12" height="12" viewBox="0 0 12 12"><path d="M2 1l2 0 1 3-1.5 1a7 7 0 0 0 3.5 3.5L8 7l3 1v2a1 1 0 0 1-1 1A9 9 0 0 1 1 2a1 1 0 0 1 1-1z" fill="#EE7325"/></svg>Phone</b>(480) 555-0192</li>
    <li style="margin-top:12px"><b><svg width="13" height="10" viewBox="0 0 13 10"><rect x=".5" y=".5" width="12" height="9" fill="#EE7325"/><path d="M1 1l5.5 4.5L12 1" stroke="#232323" fill="none"/></svg>Mail</b>hello@oakharborbuild.com</li>
  </ul></div>
  <div class="copy"><span>©Copyright 2022. <em>Oak Harbor Construction</em> | All Rights Reserved</span><span>Privacy Policy &nbsp;|&nbsp; Terms and Conditions</span></div>
</footer>

</body>
</html>
```